Visitenkarten-Design für Immobilien-Unternehmen
Designer ist sehr bemüht und die Änderungswünsche wurden rasch bearbeitet. Auch wurde im Nachhinein noch mein Wunsch auf Adaptierung zu einem Lackdruck bearbeitet und gesendet. Ich bin mit der Abwicklung vollkommen zufrieden - Vielen Dank
Zielgruppe
Die TOLU Immobilien GmbH ist eine durch Ing. Kilian Frühwald inhabergeführte Gesellschaft, welche sich schwerpunktmäßig mit Immobilieninvestitionen sowie Beteiligungen im Bereich von Wohn- und Gewerbeimmobilien beschäftigt. Das Unternehmen kauft, hält, vermietet und verkauft Liegenschaften aller Art, mit dem Fokus auf Gewerbe- und Wohnimmobilien. Zielgruppe sind Personen, welche Immobilien verkaufen möchten - wir betreiben nur eigene Vermögensverwaltung
siehe: www.tolu-immobilien.at
Aufgabenstellung
schlicht und einfach gehalten - weniger ist mehr - nur die wichtigsten Informationen auf der Visitenkarte.
siehe Homepage: www.tolu-immobilien.at

```html
<!DOCTYPE html>
<html lang="de">
<head>
<meta charset="utf-8">
<title>TOLU Immobilien GmbH – Visitenkarte</title>
<link rel="stylesheet" href="https://fonts.googleapis.com/css2?family=Open+Sans:wght@300;400;600&display=swap">
<style>
  :root {
    --stage: #3b3c3e;
    --card-dark: #323334;
    --card-light: #ffffff;
    --ink: #1a1a1a;
    --ink-soft: #3a3a3a;
    --silver: #e6e6e6;
    --rule: #222222;
  }
  * { box-sizing: border-box; margin: 0; padding: 0; }
  html, body { width: 1200px; height: 892px; overflow: hidden; }
  body {
    background: var(--stage);
    font-family: "Open Sans", sans-serif;
    position: relative;
  }
  .card {
    position: absolute;
    left: 320px;
    width: 560px;
    height: 340px;
    border-radius: 22px;
    box-shadow: 0 10px 28px rgba(0,0,0,.35);
  }
  .card--front {
    top: 60px;
    background: var(--card-dark);
    display: flex; align-items: center; justify-content: center;
  }
  .card--back {
    top: 470px;
    background: var(--card-light);
    display: flex;
    align-items: center;
    padding: 0 34px 0 40px;
    gap: 28px;
  }
  .wordmark {
    font-weight: 300;
    letter-spacing: 1px;
    line-height: 1.2;
  }
  .card--front .wordmark { color: var(--silver); font-size: 42px; }
  .card--back .wordmark {
    color: var(--ink);
    font-size: 30px;
    width: 230px;
    flex: none;
    margin-top: 60px;
  }
  .details {
    flex: 1;
    color: var(--ink-soft);
    margin-top: -30px;
  }
  .details__rule { height: 1px; background: var(--rule); }
  .details__rule--top { margin-bottom: 8px; }
  .details__rule--mid { margin: 8px 0 14px; width: 160px; }
  .person { font-weight: 600; font-size: 12px; letter-spacing: .4px; color: var(--ink); text-transform: uppercase; white-space: nowrap; }
  .company { font-size: 10px; margin-top: 2px; }
  .address { font-size: 11px; line-height: 1.45; margin-bottom: 14px; }
  .contact { list-style: none; font-size: 11px; line-height: 1.9; }
  .contact li { display: flex; align-items: center; gap: 8px; white-space: nowrap; }
  .contact svg { width: 10px; height: 10px; fill: var(--ink); flex: none; }
</style>
</head>
<body>
  <section class="card card--front">
    <p class="wordmark">TOLU Immobilien GmbH</p>
  </section>

  <section class="card card--back">
    <p class="wordmark">TOLU Immobilien GmbH</p>
    <div class="details">
      <div class="details__rule details__rule--top"></div>
      <p class="person">Ing. Kilian Frühwald</p>
      <p class="company">TOLU Immobilien GmbH</p>
      <div class="details__rule details__rule--mid"></div>
      <p class="address">Auenstraße 41/2, 8200<br>Sonnleiten</p>
      <ul class="contact">
        <li>
          <svg viewBox="0 0 10 10" aria-hidden="true"><path d="M2 0.5 L3.6 2.6 L2.8 3.6 C3.4 5 4.8 6.4 6.4 7.2 L7.4 6.4 L9.5 8 L8.4 9.5 C4.4 9.2 0.8 5.6 0.5 1.6 Z"/></svg>
          +43 664 987 21 40
        </li>
        <li>
          <svg viewBox="0 0 10 10" aria-hidden="true"><path d="M0.5 2 H9.5 V8 H0.5 Z M1.2 2.6 L5 5.4 L8.8 2.6" fill="none" stroke="#1a1a1a" stroke-width="1"/></svg>
          office@tolu-immobilien.at
        </li>
        <li>
          <svg viewBox="0 0 10 10" aria-hidden="true"><circle cx="5" cy="5" r="4.5"/><path d="M0.8 5 H9.2 M5 0.6 C3 3 3 7 5 9.4 M5 0.6 C7 3 7 7 5 9.4" fill="none" stroke="#fff" stroke-width=".6"/></svg>
          www.tolu-immobilien.at
        </li>
      </ul>
    </div>
  </section>
</body>
</html>
```